The Pixel Tap Business card.

A Simple card with our Logo and contact information. To give to investors and other professionals.

We are a nerd themed bar.
our target market is young professionals age 21+ but the real purpose of this business card is to present to potential investors and other professionals with our contact information. as we are still looking for funding before we start up.

I am partial to green and my partner likes red we are open to iteration.

Target Market(s)

Investors

Industry/Entity Type

Business

Contact Information for Business Card

Martin Hale (225) 730-6192 kent.h4711@mailnest.test Glen Porter (225) 968-5037 glenp318@mailnest.test

Font styles to use
Serif

Requirements
Nice to have
• Keep it simple but not boring.
• Use the Logos but feel free to edit them to match theme/colors.
• Keep the back clean and use one of the Logos.

```html
<!DOCTYPE html>
<html lang="en">
<head>
<meta charset="utf-8">
<title>The Pixel Tap — Business Card</title>
<link rel="stylesheet" href="https://fonts.googleapis.com/css2?family=PT+Sans:wght@400;700&display=swap">
<style>
  :root {
    --backdrop: #8f8f8f;
    --card-light: #e3e3e6;
    --ink: #000000;
    --paper-text: #ffffff;
    --accent-red: #d0202c;
    --muted-text: #e8e8e8;
  }
  * { margin: 0; padding: 0; box-sizing: border-box; }
  html, body {
    width: 1105px;
    height: 1200px;
    overflow: hidden;
    background: var(--backdrop);
    font-family: "PT Sans", Arial, sans-serif;
  }
  .canvas { position: relative; width: 1105px; height: 1200px; }
  .card {
    position: absolute;
    left: 182px;
    width: 746px;
    height: 427px;
    overflow: hidden;
  }
  .card--front { top: 119px; background: var(--card-light); }
  .card--back { top: 637px; background: var(--ink); }

  .band {
    position: absolute;
    left: 0; top: 140px;
    width: 100%; height: 145px;
  }
  .band__edge {
    position: absolute; left: 0; top: 0;
    width: 39px; height: 100%;
    background: var(--ink);
  }
  .band__contact {
    position: absolute; left: 392px; top: 0;
    width: 354px; height: 100%;
    background: var(--ink);
    color: var(--muted-text);
    padding: 20px 0 0 31px;
  }
  .contact__name {
    font-size: 25px;
    font-weight: 400;
    letter-spacing: 0.5px;
    text-transform: uppercase;
    color: var(--paper-text);
    margin-bottom: 10px;
  }
  .contact__line {
    display: flex;
    align-items: center;
    gap: 12px;
    font-size: 19px;
    height: 34px;
  }
  .contact__icon { width: 16px; height: 20px; flex: none; }

  .wordmark {
    position: absolute;
    display: flex;
    align-items: center;
    gap: 14px;
    font-weight: 700;
    font-size: 46px;
    letter-spacing: 0.5px;
    white-space: nowrap;
  }
  .wordmark__dot {
    width: 26px; height: 26px;
    border-radius: 50%;
    background: var(--accent-red);
    flex: none;
  }
  .wordmark--front {
    left: 39px; width: 353px; top: 0; height: 145px;
    justify-content: center;
    color: var(--ink);
  }
  .wordmark--back {
    left: 0; right: 0; top: 0; bottom: 0;
    justify-content: center;
    color: var(--paper-text);
    font-size: 50px;
  }
</style>
</head>
<body>
<main class="canvas">
  <section class="card card--front" aria-label="Business card front">
    <div class="band">
      <div class="band__edge"></div>
      <div class="wordmark wordmark--front">
        <span class="wordmark__dot"></span>
        <span class="wordmark__name">The Pixel Tap</span>
      </div>
      <div class="band__contact">
        <p class="contact__name">Martin Hale</p>
        <p class="contact__line">
          <svg class="contact__icon" viewBox="0 0 16 20" aria-hidden="true">
            <rect x="3" y="1" width="10" height="18" rx="1.5" fill="none" stroke="#e8e8e8" stroke-width="1.6"/>
            <line x1="6.5" y1="16" x2="9.5" y2="16" stroke="#e8e8e8" stroke-width="1.4"/>
          </svg>
          <span>(225) 730-6192</span>
        </p>
        <p class="contact__line">
          <svg class="contact__icon" viewBox="0 0 16 20" aria-hidden="true">
            <rect x="1" y="5" width="14" height="10" fill="none" stroke="#e8e8e8" stroke-width="1.4"/>
            <polyline points="1,5 8,11 15,5" fill="none" stroke="#e8e8e8" stroke-width="1.4"/>
          </svg>
          <span>kent.h4711@mailnest.test</span>
        </p>
      </div>
    </div>
  </section>

  <section class="card card--back" aria-label="Business card back">
    <div class="wordmark wordmark--back">
      <span class="wordmark__dot"></span>
      <span class="wordmark__name">The Pixel Tap</span>
    </div>
  </section>
</main>
</body>
</html>
```